User help guide for software for investment bank

We need a professional design for our user help guides for new software we have written for our client. We develop visualization software for investment banks in Singapore mainly focused in the financial and risk management area. Our help guides are design to show them how the software works as well as promote our brand
Updates

Target Market(s)

Investment banking, risk management, finance

Industry/Entity Type

Bank

Requirements
Must have
• Content of document and logos
• Colour sheme
• Professional brouchure design
• Verindo and plunox logos on it
• Look at www.verindo-example.com for company looks and feel
• PLEASE USE COLOUR SCHEMES BELOW IN ATTACHMENT AND FOLLOW SIMILAR STYLE TO CLIENT ANNUAL REPORT

```html
<!DOCTYPE html>
<html lang="en">
<head>
<meta charset="utf-8">
<title>Contents – User Help Guide</title>
<link href="https://fonts.googleapis.com/css2?family=Open+Sans:wght@300;700&display=swap" rel="stylesheet">
<style>
  :root {
    --page-bg: #ffffff;
    --heading-blue: #1f3f73;
    --rule-blue: #4a6a9a;
    --toc-text: #5a5a5a;
    --photo-dark: #14101c;
    --photo-violet: #9a6fd0;
    --photo-pink: #e7b8d8;
    --photo-teal: #4a9e8a;
  }
  html, body {
    margin: 0;
    padding: 0;
    overflow: hidden;
  }
  body {
    width: 849px;
    height: 1200px;
    background: var(--page-bg);
    position: relative;
    font-family: "Open Sans", sans-serif;
  }
  .hero-photo {
    position: absolute;
    left: 0;
    top: 0;
    width: 849px;
    height: 600px;
    background:
      linear-gradient(180deg, rgba(20,16,28,0) 50%, rgba(20,16,28,0.95) 78%, var(--photo-dark) 100%),
      radial-gradient(ellipse at 40% 30%, var(--photo-pink) 0%, var(--photo-violet) 45%, #3b2a55 75%),
      var(--photo-dark);
  }
  .contents {
    position: absolute;
    left: 58px;
    top: 636px;
    width: 734px;
  }
  .contents-title {
    margin: 0;
    font-weight: 700;
    font-size: 35px;
    line-height: 40px;
    color: var(--heading-blue);
  }
  .contents-rule {
    position: absolute;
    left: 0;
    top: 42px;
    width: 734px;
    height: 1px;
    background: var(--rule-blue);
  }
  .toc-entry {
    position: absolute;
    left: 0;
    width: 734px;
    font-weight: 300;
    font-size: 22px;
    line-height: 26px;
    color: var(--toc-text);
    display: flex;
    justify-content: space-between;
  }
  .toc-entry.level-2 .toc-label { padding-left: 28px; }
  .toc-entry.level-3 .toc-label { padding-left: 59px; }
</style>
</head>
<body>
  <div class="hero-photo" role="img" aria-label="Photo of a speaker presenting on stage at a software conference, with large screens and a seated audience"></div>

  <section class="contents">
    <h1 class="contents-title">Contents</h1>
    <div class="contents-rule"></div>

    <div class="toc-entry level-1" style="top:61px"><span class="toc-label">1.&nbsp; User Roles and Permissions</span><span>3</span></div>
    <div class="toc-entry level-1" style="top:112px"><span class="toc-label">2.&nbsp; Restrictions using Web Editor Tool</span><span>3</span></div>
    <div class="toc-entry level-1" style="top:162px"><span class="toc-label">3.&nbsp; Navigation</span><span>4</span></div>
    <div class="toc-entry level-2" style="top:187px"><span class="toc-label">a.&nbsp; Data and Analytics pane</span><span>4</span></div>
    <div class="toc-entry level-3" style="top:212px"><span class="toc-label">1.1.1&nbsp; Data Pane</span><span>5</span></div>
    <div class="toc-entry level-3" style="top:237px"><span class="toc-label">1.1.2&nbsp; Analytics pane</span><span>5</span></div>
    <div class="toc-entry level-2" style="top:262px"><span class="toc-label">b.&nbsp; TOOLBAR</span><span>6</span></div>
    <div class="toc-entry level-2" style="top:287px"><span class="toc-label">c.&nbsp; Columns and Rows</span><span>7</span></div>
    <div class="toc-entry level-2" style="top:312px"><span class="toc-label">d.&nbsp; Marks</span><span>8</span></div>
    <div class="toc-entry level-2" style="top:337px"><span class="toc-label">e.&nbsp; FILTERS</span><span>9</span></div>
    <div class="toc-entry level-1" style="top:388px"><span class="toc-label">4.&nbsp; Calculated Fields</span><span>9</span></div>
  </section>
</body>
</html>
```